Dietitian needs a new business card design

I need a new business card design for my nutrition business that provides individual clinical nutrition advice for people with medical conditions. Business cards will be handed out to doctors, specialists and clients so will need to be sharp and project an image of professionalism

Target Market(s)

My clients are typically referred by doctors or specialists and the card will be used to handout to clients and their doctors.

Industry/Entity Type

Medical

Contact Information for Business Card

The business card will require the details below. These details can be found from my website https://www.tamberlydietitian.com.au/

Font styles to use
Serif

Colors

Designer to choose colors to be used in the design.

Requirements
Must have
• 1. It needs be professional and contemporary
• 2. It needs to incorporate my logo
• 3. It needs space to write appointment times and dates
• 4. It needs to provide my phone number, fax number, email address and my web address
Nice to have
• Include the Endorsed Clinical Dietitian Logo
• I have access to Pixorra if required
• The locations I practise from
Should not have
• Pictures of food
• Spelling MIstakes

```html
<!DOCTYPE html>
<html lang="en">
<head>
<meta charset="utf-8">
<title>Harbourline Nutrition &amp; Dietetics – Business Card</title>
<link href="https://fonts.googleapis.com/css2?family=Roboto:wght@400;500;700&display=swap" rel="stylesheet">
<style>
  :root {
    --backdrop: #2b2b2b;
    --card: #f3f3f3;
    --brand-blue: #0b5aa6;
    --brand-green: #8cc63f;
    --ink: #4a4a4a;
    --rule: #555555;
    --badge: #f47b20;
  }
  * { box-sizing: border-box; margin: 0; padding: 0; }
  html, body { width: 1200px; height: 960px; overflow: hidden; }
  body {
    background: var(--backdrop);
    font-family: "Roboto", Arial, sans-serif;
    position: relative;
  }
  .card {
    position: absolute;
    width: 600px;
    height: 343px;
    background: var(--card);
    border-radius: 22px;
  }
  .card--front { left: 302px; top: 128px; }
  .card--back  { left: 299px; top: 508px; }

  .credential-badge {
    position: absolute;
    left: 500px; top: 33px;
    width: 74px; height: 35px;
    background: var(--badge);
    border-radius: 2px;
  }
  .front-mark {
    position: absolute;
    left: 0; right: 0; top: 64px;
    display: flex; justify-content: center;
  }
  .front-mark__dot {
    width: 72px; height: 72px; border-radius: 50%;
    background: var(--brand-green);
  }
  .holder-name {
    position: absolute; left: 0; right: 0; top: 162px;
    text-align: center;
    font-size: 23px; font-weight: 700;
    color: var(--brand-blue);
  }
  .holder-title {
    position: absolute; left: 0; right: 0; top: 189px;
    text-align: center;
    font-size: 15px; font-weight: 500;
    color: var(--brand-green);
  }
  .contact {
    position: absolute; left: 0; right: 0; top: 222px;
    text-align: center;
    font-size: 14.5px; line-height: 20.5px;
    color: var(--ink);
  }

  .brand-lockup {
    position: absolute; left: 0; right: 0; top: 58px;
    display: flex; align-items: center; justify-content: center; gap: 14px;
  }
  .brand-lockup__dot {
    width: 70px; height: 70px; border-radius: 50%;
    background: var(--brand-green);
  }
  .brand-lockup__name {
    font-size: 24px; font-weight: 500;
    color: var(--brand-blue);
    width: 200px; line-height: 28px;
  }

  .appointments {
    position: absolute; left: 66px; top: 186px;
    width: 460px;
  }
  .appointment {
    display: flex; align-items: flex-end;
    height: 22px; margin-bottom: 22px;
    font-size: 15.5px; color: var(--ink);
  }
  .appointment__rule {
    border-bottom: 1px solid var(--rule);
    height: 12px; margin-bottom: 3px;
  }
  .appointment__rule--date { width: 186px; margin-left: 4px; margin-right: 19px; }
  .appointment__rule--time { width: 121px; margin-left: 2px; margin-right: 7px; }
</style>
</head>
<body>
  <section class="card card--front" aria-label="Card front">
    <div class="credential-badge" aria-label="Endorsed Clinical Dietitian badge"></div>
    <div class="front-mark"><span class="front-mark__dot"></span></div>
    <h1 class="holder-name">Daniel Whitcombe</h1>
    <p class="holder-title">Accredited Nutritionist</p>
    <p class="contact">
      Tel: 0412 555 301 Fax: +613 6300 4417<br>
      daniel@tamberlydietitian.com.au | www.tamberlydietitian.com.au<br>
      Tamberly&nbsp; | Elmvale&nbsp; | Cooper's Bend&nbsp; | Ashdown
    </p>
  </section>

  <section class="card card--back" aria-label="Card back">
    <div class="brand-lockup">
      <span class="brand-lockup__dot"></span>
      <span class="brand-lockup__name">Harbourline Nutrition &amp; Dietetics</span>
    </div>
    <div class="appointments">
      <div class="appointment"><span>Date</span><span class="appointment__rule appointment__rule--date"></span><span>Time</span><span class="appointment__rule appointment__rule--time"></span><span>am/pm</span></div>
      <div class="appointment"><span>Date</span><span class="appointment__rule appointment__rule--date"></span><span>Time</span><span class="appointment__rule appointment__rule--time"></span><span>am/pm</span></div>
      <div class="appointment"><span>Date</span><span class="appointment__rule appointment__rule--date"></span><span>Time</span><span class="appointment__rule appointment__rule--time"></span><span>am/pm</span></div>
    </div>
  </section>
</body>
</html>
```